Corvellis IP Access Control Data Sheet

Initially we are looking for a better and consistent ( cleaner / corporate) layout / design of the attached A4 Data Sheet and A5 mini flyer. Going forward we would then be looking to create a Brochure & flyers and some other items ( wall displays, banners etc.)
Target Market(s)
Our customers are end -users and security equipment installers
Industry/Entity Type
Cleaner
Font styles to use
Sans Serif
Requirements
Must have
- 1. Better images of devices ( pc, laptop , tablet, smartphone etc.) with clearer screen shots of the software
- 2. A consistent them across all literature
- 3. Designs must be print ready and in an editable format (PSD , GIMP etc.)

```html
<!DOCTYPE html>
<html lang="en">
<head>
<meta charset="utf-8">
<title>Corvellis IP – Access Control Data Sheet</title>
<link rel="stylesheet" href="https://fonts.googleapis.com/css2?family=Bebas+Neue&family=Montserrat:wght@400;500&family=Roboto:wght@300;400&display=swap">
<style>
  :root {
    --teal: #00918d;
    --teal-deep: #00827e;
    --paper: #ebebeb;
    --ink: #2f2f2f;
    --ink-soft: #4a4a4a;
    --rule: #c9c9c9;
    --rule-light: rgba(255,255,255,0.28);
    --white: #ffffff;
    --stage: #ffffff;
  }
  * { box-sizing: border-box; margin: 0; padding: 0; }
  html, body { width: 1200px; height: 1200px; overflow: hidden; background: var(--stage); }
  .sheet {
    position: absolute; left: 210px; top: 50px;
    width: 780px; height: 1100px;
    background: var(--paper);
    box-shadow: 0 6px 24px rgba(0,0,0,0.18);
    overflow: hidden;
  }
  .cover {
    position: absolute; left: 0; top: 0; width: 100%; height: 745px;
    background: linear-gradient(160deg, var(--teal) 0%, var(--teal-deep) 100%);
  }
  .cover__rule {
    position: absolute; left: 0; right: 0; top: 110px;
    height: 1px; background: var(--rule-light);
  }
  .brand {
    position: absolute; left: 0; top: 255px;
    display: flex; align-items: center; gap: 18px;
  }
  .brand__mark { width: 118px; height: 118px; background: var(--ink); }
  .brand__name {
    font-family: "Montserrat", sans-serif; font-weight: 400;
    color: var(--white); font-size: 38px; letter-spacing: 2px; line-height: 1;
  }
  .brand__tag {
    font-family: "Montserrat", sans-serif; font-weight: 400;
    color: var(--white); font-size: 13px; letter-spacing: 0.5px; margin-top: 8px;
  }
  .headline {
    position: absolute; left: 60px; top: 515px;
    font-family: "Bebas Neue", sans-serif; font-weight: 400; color: var(--white);
    font-size: 62px; line-height: 1.04; letter-spacing: 1.5px;
    white-space: nowrap;
  }
  .contacts {
    position: absolute; left: 60px; right: 60px; top: 790px;
    display: flex; justify-content: space-between; gap: 30px;
  }
  .contact {
    flex: 1; display: flex; align-items: center; gap: 12px;
    padding-bottom: 14px; border-bottom: 1px solid var(--rule);
    font-family: "Roboto", sans-serif; font-weight: 400;
    font-size: 18px; color: var(--ink-soft); white-space: nowrap;
  }
  .contact svg { width: 20px; height: 20px; flex: none; }
  .company {
    position: absolute; left: 60px; right: 60px; top: 920px;
    display: flex; align-items: center; gap: 32px;
    padding-bottom: 26px; border-bottom: 1px solid var(--rule);
  }
  .company__logo { display: flex; align-items: center; gap: 10px; flex: none; }
  .company__logo-square { width: 30px; height: 30px; background: var(--teal); }
  .company__logo-name {
    font-family: "Montserrat", sans-serif; font-weight: 500;
    font-size: 44px; color: var(--teal); letter-spacing: 4px;
  }
  .company__address {
    font-family: "Roboto", sans-serif; font-weight: 300;
    font-size: 13.5px; line-height: 1.6; color: var(--ink-soft);
    white-space: nowrap;
  }
</style>
</head>
<body>
  <main class="sheet">
    <section class="cover">
      <div class="cover__rule"></div>
      <div class="brand">
        <div class="brand__mark"></div>
        <div>
          <div class="brand__name">CORVELLIS IP</div>
          <div class="brand__tag">DOOR ACCESS CONTROL SYSTEM</div>
        </div>
      </div>
      <h1 class="headline">Access Control<br>From a Single Standalone<br>Door to a 200 Door Network</h1>
    </section>

    <div class="contacts">
      <div class="contact">
        <svg viewBox="0 0 24 24" fill="none" stroke="#4a4a4a" stroke-width="1.6"><circle cx="12" cy="12" r="10"/><ellipse cx="12" cy="12" rx="4.5" ry="10"/><path d="M2 12h20M4 7h16M4 17h16"/></svg>
        www.corvellisip.co.uk
      </div>
      <div class="contact">
        <svg viewBox="0 0 24 24" fill="none" stroke="#4a4a4a" stroke-width="1.6"><rect x="2" y="5" width="20" height="14" rx="1"/><path d="M2 6l10 7 10-7"/></svg>
        sales@hmsltd.co.uk
      </div>
      <div class="contact">
        <svg viewBox="0 0 24 24" fill="#2f2f2f"><path d="M6.6 10.8a15 15 0 006.6 6.6l2.2-2.2a1 1 0 011-.25 11.4 11.4 0 003.6.6 1 1 0 011 1V20a1 1 0 01-1 1A17 17 0 013 4a1 1 0 011-1h3.5a1 1 0 011 1c0 1.25.2 2.45.6 3.6a1 1 0 01-.25 1z"/></svg>
        01632 960 418
      </div>
    </div>

    <div class="company">
      <div class="company__logo">
        <div class="company__logo-square"></div>
        <div class="company__logo-name">HMS</div>
      </div>
      <p class="company__address">Halden Marsh Systems Ltd.<br>T/A HMS. 12 Fenwick Road. Brookmere Trading Estate. Alderby. AB1 2CD</p>
    </div>
  </main>
</body>
</html>
```